Business Card Design and Stationary design for consulting firm

Harbourline Sourcing are looking for a new business card design and a design for their A4 letterhead / A4 invoices.

We are seeking to heavily increase our brand awareness and require a business card that's professional in appearance but also shows flare and innovation. A card design that people will remember.

About Us
Harbourline Sourcing are `The Sourcing Crew’.
Our mission is to be one of Australia’s greatest companies. Our aim is to help our customers achieve the best result from their purchasing experience.

Our Requirement:
• IMPACT! IMPACT! IMPACT!
• BUSINESS & PROFESSIONAL LOOKING

• Our business colours are orange, blue and green (See the logo attached).

We have provided an Art Design specification (attached) that needs to be followed for you to win the design. This also has the font, which is used on the logo.

We are after a two sided business card

Side One should have the:
The company Logo
The Sourcing Crew
www.harbourlinesourcing.com.au
Procure | Personnel | Probity & Privacy
Sydney | Melbourne | Adelaide | Brisbane

Side Two
Logo (optional)
Harbourline Sourcing (optional)
Employee details (details listed below)

The above format is our preferred option, but if you think you can come up with something better, feel free to put it forward.

We are leaving the design up to you, but it must incorporate the logo.

We will need a template that we can change the employee details on, as we will be adding more staff over the coming months.

The details below are for one employee per card with the same design.
------------------------

Employee Details:

Marcus Del Arroyo MBA, MMgmtStratProc
Principal Consultant
0491 372 618
Marcus@harbourlinesourcing.com.au

Brianna Tolley
Consulting Manager
0462 915 308
Brianna@harbourlinesourcing.com.au

Our website is www.harbourlinesourcing.com.au

The Letterhead / invoice needs to incorporate:
the company Logo
The Sourcing Crew
Sydney | Melbourne | Adelaide | Brisbane but otherwise the design is over to you.

This file needs to be delivered in word format as other detail will be added to the documents.

We look forward to you award winning designs. If you require any further information please feel free to contact us.

Regards
Harbourline Sourcing

Target Market(s)

Our Target market is companies with 80+ employees. The market we segment is heavily male based, between the ages of 35-55 years of age.

Industry/Entity Type

Consulting

Contact Information for Business Card

See Project Description

Font styles to use
Other font styles liked:
• See Art Specification

Requirements
Must have
• Company Colours, See Project Description
Should not have
• Be outside the Art specification guidelines

```html
<!DOCTYPE html>
<html lang="en">
<head>
<meta charset="utf-8">
<title>Harbourline Sourcing — Business Card</title>
<link rel="stylesheet" href="https://fonts.googleapis.com/css2?family=Open+Sans:wght@400;600;700&display=swap">
<style>
  :root {
    --page-bg: #e6e4e0;
    --card-white: #ffffff;
    --panel-dark: #3b3b3d;
    --brand-orange: #f47a20;
    --brand-blue: #2a8fd4;
    --brand-green: #5db53f;
    --ink-grey: #4a4a4c;
    --ink-light: #f2f2f2;
  }
  * { box-sizing: border-box; margin: 0; padding: 0; }
  html, body {
    width: 1200px; height: 950px; overflow: hidden;
    background: var(--page-bg);
    font-family: "Open Sans", Arial, sans-serif;
  }
  .card {
    position: absolute; top: 125px;
    width: 400px; height: 700px;
    background: var(--card-white);
    box-shadow: 0 6px 18px rgba(0,0,0,0.18);
    overflow: hidden;
  }
  .card--front { left: 170px; }
  .card--back { left: 630px; }

  .wordmark {
    position: absolute; display: flex; align-items: center; gap: 10px;
    color: var(--ink-grey); font-weight: 700; letter-spacing: 0.3px; white-space: nowrap;
  }
  .wordmark__dot { border-radius: 50%; background: var(--brand-blue); flex: none; }
  .card--front .wordmark { left: 0; right: 0; justify-content: center; top: 190px; font-size: 26px; }
  .card--front .wordmark__dot { width: 22px; height: 22px; }
  .card--back .wordmark { left: 36px; top: 70px; font-size: 20px; }
  .card--back .wordmark__dot { width: 18px; height: 18px; }

  .front-info {
    position: absolute; right: 40px; bottom: 60px;
    font-size: 14.5px; line-height: 1.55; color: var(--ink-grey); white-space: nowrap;
  }
  .front-info__tagline { color: var(--brand-orange); font-weight: 600; font-size: 16px; }
  .front-info__web { color: var(--brand-blue); }

  .back-panel { position: absolute; inset: 0; width: 400px; height: 700px; }

  .staff {
    position: absolute; left: 110px; top: 390px;
    color: var(--ink-light); font-size: 13px; line-height: 1.6; white-space: nowrap;
  }
  .staff__name { color: var(--brand-blue); font-size: 21px; font-weight: 600; text-transform: uppercase; line-height: 1.25; }
  .staff__quals { color: var(--brand-orange); font-size: 12px; text-transform: uppercase; }
  .staff__role { color: var(--brand-orange); font-size: 14px; text-transform: uppercase; letter-spacing: 0.5px; margin-bottom: 16px; }
  .staff__line { display: flex; align-items: center; gap: 8px; }
  .staff__icon { width: 14px; height: 14px; flex: none; }
</style>
</head>
<body>

<section class="card card--front" aria-label="Card front">
  <div class="wordmark"><span class="wordmark__dot"></span>Harbourline Sourcing</div>
  <div class="front-info">
    <p class="front-info__tagline">The Sourcing Crew</p>
    <p class="front-info__web">www.harbourlinesourcing.com.au</p>
    <p>Procure • Personnel • Probity &amp; Privacy</p>
    <p>Sydney • Melbourne • Adelaide • Brisbane</p>
  </div>
</section>

<section class="card card--back" aria-label="Card back">
  <svg class="back-panel" viewBox="0 0 400 700" aria-hidden="true">
    <polygon points="32,334 400,298 400,700 112,700 36,482 47,472" fill="var(--panel-dark)"/>
    <line x1="26" y1="332" x2="400" y2="295" stroke="var(--brand-orange)" stroke-width="5"/>
    <polyline points="28,334 44,472 32,482" fill="none" stroke="var(--brand-blue)" stroke-width="5"/>
    <line x1="32" y1="482" x2="108" y2="700" stroke="var(--brand-green)" stroke-width="5"/>
  </svg>

  <div class="wordmark"><span class="wordmark__dot"></span>Harbourline Sourcing</div>

  <div class="staff">
    <p class="staff__name">Marcus Del Arroyo</p>
    <p class="staff__quals">MBA, MMgmtStratProc</p>
    <p class="staff__role">Principal Consultant</p>
    <p class="staff__line">
      <svg class="staff__icon" viewBox="0 0 16 16" aria-hidden="true"><path d="M4 1h3l1 4-2 1.5a9 9 0 0 0 3.5 3.5L11 8l4 1v3a2 2 0 0 1-2 2C6.5 14 2 9.5 2 3a2 2 0 0 1 2-2z" fill="var(--brand-blue)"/></svg>
      0491 372 618
    </p>
    <p class="staff__line">
      <svg class="staff__icon" viewBox="0 0 16 16" aria-hidden="true"><rect x="1" y="3" width="14" height="10" rx="1" fill="var(--brand-blue)"/><path d="M1.5 3.5 8 9l6.5-5.5" fill="none" stroke="var(--panel-dark)" stroke-width="1.3"/></svg>
      Marcus@harbourlinesourcing.com.au
    </p>
    <p class="staff__line">
      <svg class="staff__icon" viewBox="0 0 16 16" aria-hidden="true"><circle cx="8" cy="8" r="7" fill="var(--brand-blue)"/><path d="M1 8h14M8 1c-3 3.5-3 10.5 0 14M8 1c3 3.5 3 10.5 0 14" fill="none" stroke="var(--panel-dark)" stroke-width="1"/></svg>
      www.harbourlinesourcing.com.au
    </p>
  </div>
</section>

</body>
</html>
```